812 EDDM FLYER FOR CARPET CLEANING & WINDOW WASHING

Full Size Double Sided full color EDDM mailer

****PLEASE MAKE FONT TYPE, SIZE, COLOR, SPACING SAME AS IS EXAMPLE FLYER*******

***I have uploaded LOGO... It is on the VAN WRAP 812 CLEANING & RESTORATION

I have included an EDDM flyer and want my flyer to look like the example I uploaded.

I wanted to make it look Better & add my images and content. I have included the content under Must Haves......

Raindrop background

****Not all images will be used. Each service requires 2 images as seen on examply flyer... Please pic best 2 for each service, I can purchase new stock photo if needed

Target Market(s)

Residential Home Owners

Industry/Entity Type

Cleaning Service

Font styles to use
Serif

Colors
0555a3
ec1f27
fbed22
ffc214

Requirements
Must have
• Look Like Example EDDM postcard uploaded
• My images & content
• CARPET CLEANING Safe Eco-Friendly Truck Mounted Steam Cleaning. Say goodbye to those ugly carpet stains.
• WINDOW WASHING Interior/Exterior & Screens. Crystal Clear & Streak Free Windows
• POWER WASHING: Soft Wash & Power Wash. Safely cleans
• WATER DAMAGE: Got Mold or Water damage? Free IR Imaging Detection
• TILE & GROUT: Clean, Restore & Rejuvenate Tile, Grout & Stone
• MAINTENANCE: Professional & dependable repairs. We can Fit It!
• Call Today! 858-555-0147
• www.TidyNorth812.example
• ECO FRIENDLY CLEANING
• San Diego’s Trusted Cleaning Specialists

```html
<!DOCTYPE html>
<html lang="en">
<head>
<meta charset="utf-8">
<title>812 Cleaning &amp; Restoration – Free Estimates Mailer</title>
<link href="https://fonts.googleapis.com/css2?family=Arvo:ital,wght@0,700;1,700&family=Montserrat:ital,wght@1,800;1,900&family=Roboto+Condensed:ital,wght@1,500&display=swap" rel="stylesheet">
<style>
  :root{
    --stage:#e7e8ea;
    --blue:#0a5cc0;
    --blue-light:#1c74d6;
    --blue-deep:#0a4399;
    --navy:#0b3f8a;
    --white:#ffffff;
    --sky-text:#8fd0ff;
    --label-band:rgba(10,55,130,0.85);
  }
  *{margin:0;padding:0;box-sizing:border-box}
  html,body{width:1200px;height:870px;overflow:hidden;background:var(--stage)}
  .mailer{
    position:absolute;left:0;top:35px;width:1200px;height:800px;overflow:hidden;
    background:radial-gradient(ellipse at 50% 40%,var(--blue-light),var(--blue) 70%);
  }
  .headline-band{
    position:absolute;left:0;top:54px;width:100%;height:188px;
    background:linear-gradient(180deg,var(--blue-light),var(--blue-deep));
    border-top:2px solid rgba(255,255,255,.8);
    border-bottom:2px solid rgba(255,255,255,.6);
  }
  .pill{
    position:absolute;left:284px;width:629px;border-radius:36px;z-index:3;
    display:flex;align-items:center;justify-content:center;
    font-family:"Arvo",serif;font-weight:700;font-style:italic;white-space:nowrap;
  }
  .pill--offer{top:19px;height:70px;background:var(--navy);border:3px solid var(--white);color:var(--white);font-size:33px}
  .pill--services{top:208px;height:68px;background:var(--white);color:var(--navy);font-size:40px;box-shadow:0 3px 8px rgba(0,0,0,.3)}
  .pill--services u{text-decoration-thickness:3px;text-underline-offset:4px}
  .free-estimates{
    position:absolute;left:0;width:100%;top:88px;text-align:center;z-index:2;
    font-family:"Montserrat",sans-serif;font-weight:900;font-style:italic;
    font-size:121px;letter-spacing:-3px;color:var(--white);line-height:1;
    text-shadow:0 4px 8px rgba(0,0,0,.35);
  }
  .services{
    position:absolute;left:62px;top:254px;width:1075px;z-index:1;
    display:grid;grid-template-columns:repeat(3,1fr);grid-template-rows:170px 167px;gap:13px 17px;
  }
  .service{position:relative;border:2px solid var(--white);border-radius:14px;overflow:hidden}
  .service__photo{position:absolute;inset:0}
  .service__label{
    position:absolute;left:0;right:0;bottom:0;height:32px;background:var(--label-band);
    display:flex;align-items:center;justify-content:center;
    font-family:"Arvo",serif;font-weight:700;font-style:italic;font-size:20px;color:var(--white);
  }
  .van{position:absolute;left:35px;top:612px;width:462px;height:172px;border-radius:40px 60px 20px 20px;
    background:linear-gradient(90deg,#1d5fb8,#c9d8ea 70%,#e8eef5)}
  .call-today{
    position:absolute;left:512px;top:632px;font-family:"Arvo",serif;font-weight:700;font-size:26px;color:var(--white);
    line-height:1;transform:rotate(-9deg);transform-origin:left bottom;white-space:nowrap;
  }
  .phone{
    position:absolute;left:540px;top:652px;font-family:"Montserrat",sans-serif;font-weight:800;font-style:italic;
    font-size:60px;letter-spacing:-2px;color:var(--white);line-height:1;white-space:nowrap;
  }
  .website{
    position:absolute;left:545px;top:712px;font-family:"Arvo",serif;font-weight:700;font-size:29px;color:var(--white);line-height:1;white-space:nowrap;
  }
  .look-back{position:absolute;left:1005px;top:643px;width:160px;height:94px}
  .look-back__text{
    position:absolute;left:8px;top:8px;width:132px;text-align:center;
    font-family:"Roboto Condensed",sans-serif;font-weight:500;font-style:italic;font-size:20px;line-height:26px;color:var(--navy);
  }
  .tagline{
    position:absolute;left:541px;top:756px;font-family:"Arvo",serif;font-weight:700;font-style:italic;
    font-size:24px;letter-spacing:2.4px;color:var(--sky-text);white-space:nowrap;
  }
</style>
</head>
<body>
<main class="mailer">
  <div class="headline-band"></div>
  <div class="pill pill--offer">Don't Miss Out! We're Offering:</div>
  <h1 class="free-estimates">FREE ESTIMATES</h1>
  <div class="pill pill--services">On&nbsp;<u>ALL</u>&nbsp;of Our Services!</div>

  <section class="services">
    <div class="service"><div class="service__photo" role="img" aria-label="Photo of a technician steam cleaning carpet" style="background:linear-gradient(180deg,#dcd9cf,#b9b3a4)"></div><div class="service__label">CARPET CLEANING</div></div>
    <div class="service"><div class="service__photo" role="img" aria-label="Photo of a worker squeegeeing a window from a ladder" style="background:linear-gradient(180deg,#9eb3bd,#3d4a52)"></div><div class="service__label">WINDOW WASHING</div></div>
    <div class="service"><div class="service__photo" role="img" aria-label="Photo of a worker power washing a tile roof" style="background:linear-gradient(160deg,#c9643a,#7a3a22 70%,#8fae7a)"></div><div class="service__label">POWER WASHING</div></div>
    <div class="service"><div class="service__photo" role="img" aria-label="Photo of a moisture meter on a tiled wall" style="background:linear-gradient(180deg,#e6e4dc,#a9a79d)"></div><div class="service__label">WATER DAMAGE</div></div>
    <div class="service"><div class="service__photo" role="img" aria-label="Photo of a technician cleaning tile and grout" style="background:linear-gradient(180deg,#b69a78,#d9c3a2)"></div><div class="service__label">TILE &amp; GROUT</div></div>
    <div class="service"><div class="service__photo" role="img" aria-label="Photo of a handyman tool belt in a framed room" style="background:linear-gradient(90deg,#3a3a40,#d9c7a6)"></div><div class="service__label">MAINTENANCE</div></div>
  </section>

  <div class="van" role="img" aria-label="Illustration of the 812 Cleaning &amp; Restoration wrapped service van"></div>

  <div class="call-today">Call Today</div>
  <div class="phone">858-555-0147</div>
  <div class="website">www.TidyNorth812.example</div>

  <div class="look-back">
    <svg width="160" height="94" viewBox="0 0 160 94" aria-hidden="true">
      <defs><linearGradient id="tagFill" x1="0" x2="1"><stop offset="0" stop-color="#3a7fd6"/><stop offset=".45" stop-color="#ffffff"/><stop offset="1" stop-color="#ffffff"/></linearGradient></defs>
      <polygon points="0,0 140,0 160,47 140,94 0,94" fill="url(#tagFill)"/>
    </svg>
    <div class="look-back__text">Look on back to see what we can do for you!</div>
  </div>

  <div class="tagline">San Diego's Trusted Cleaning Specialists</div>
</main>
</body>
</html>
```